Business card for Chiropractic clinics needs reworked / redesigned

The business card in attachment was designed 10 years ago. It is in need of an update.
We have 2 clinics:
VELDHOVE KLINIEK & VELDHOVE KLINIEK NOORD
Only one address needs to be on the card for doctors that only work in one clinic and two addresses need to be on the card for the doctors that work in both clinics.

Target Market(s)

patients/referrers

Industry/Entity Type

Medical

Contact Information for Business Card

Logo (in full or zoomed-in)
Clinic Name
Doctor name and title
clinic address, website, tel, email

Font styles to use
Sans Serif

Colors

Designer to choose colors to be used in the design.

Requirements
Must have
• Good contrast/readability
• We like modern minimalistic designs
• The Bcard needs to project our very high standard of proficiency/professionalism
Should not have
• Not curly
• Not to much colours

```html
<!DOCTYPE html>
<html lang="nl">
<head>
<meta charset="utf-8">
<title>Veldhove Kliniek – visitekaartje</title>
<link href="https://fonts.googleapis.com/css2?family=Lato:wght@300;400;700;900&display=swap" rel="stylesheet">
<style>
  :root {
    --ink: #01252a;
    --paper: #ffffff;
    --stage: #eceeee;
    --grey: #8a8c8e;
    --text: #0c2a2e;
  }
  html, body {
    margin: 0;
    padding: 0;
    width: 1200px;
    height: 900px;
    overflow: hidden;
    background: var(--stage);
    font-family: "Lato", Arial, sans-serif;
  }
  .sheet {
    width: 1200px;
    height: 900px;
    display: flex;
    align-items: center;
    justify-content: center;
    gap: 60px;
  }
  .card {
    position: relative;
    width: 520px;
    height: 310px;
    box-shadow: 0 6px 18px rgba(0, 0, 0, 0.18);
    overflow: hidden;
  }
  .card--front {
    background: var(--ink);
    display: flex;
    align-items: center;
    justify-content: center;
  }
  .brand-name {
    color: var(--paper);
    font-weight: 700;
    font-size: 22px;
    letter-spacing: 0.14em;
  }
  .card--back {
    background: var(--paper);
    color: var(--text);
  }
  .card__wave {
    position: absolute;
    left: 0;
    bottom: 0;
    width: 520px;
    height: 310px;
  }
  .card__brand {
    position: absolute;
    top: 34px;
    right: 34px;
    font-weight: 700;
    font-size: 15px;
    letter-spacing: 0.14em;
    color: var(--ink);
  }
  .contact {
    position: absolute;
    top: 34px;
    left: 38px;
  }
  .contact__name {
    margin: 0;
    font-weight: 900;
    font-size: 19px;
    letter-spacing: 0.02em;
  }
  .contact__title {
    margin: 2px 0 14px 12px;
    font-weight: 300;
    font-size: 14px;
    letter-spacing: 0.05em;
  }
  .clinic {
    margin: 0 0 8px 22px;
    font-size: 13.5px;
    line-height: 1.25;
  }
  .clinic__name { font-weight: 400; letter-spacing: 0.02em; }
</style>
</head>
<body>
  <main class="sheet">
    <section class="card card--front">
      <span class="brand-name">VELDHOVE</span>
    </section>

    <section class="card card--back">
      <svg class="card__wave" viewBox="0 0 520 310" aria-hidden="true">
        <path d="M0 262 C150 300 300 190 520 150 L520 310 L0 310 Z" fill="var(--grey)"/>
        <path d="M0 268 C120 312 300 176 520 136 L520 146 C320 190 170 290 0 276 Z" fill="var(--paper)"/>
        <path d="M0 282 C160 300 320 168 520 140 L520 310 L0 310 Z" fill="var(--ink)"/>
      </svg>
      <span class="card__brand">VELDHOVE</span>
      <div class="contact">
        <h1 class="contact__name">PIETER VANDAMME</h1>
        <p class="contact__title">CHIROPRACTOR</p>
        <p class="clinic">
          <span class="clinic__name">VELDHOVE KLINIEK</span><br>
          Lindenlaan 48<br>
          09 555 01 24<br>
          veldhovekliniek.be
        </p>
        <p class="clinic">
          <span class="clinic__name">VELDHOVE KLINIEK NOORD</span><br>
          Molenstraat 17<br>
          09 555 07 86<br>
          veldhovenoord.be
        </p>
      </div>
    </section>
  </main>
</body>
</html>
```